Business Card Design Project

See the detainl of the Fernlo company project I also have live: http://tasks.plomwerk.com/task.aspx?id=384920

Reason: I am waiting to select a logo design and ideally the business card design will be from the same person

```html
<!DOCTYPE html>
<html lang="en">
<head>
<meta charset="utf-8">
<title>Fernlo LLP – Business Card</title>
<link rel="stylesheet" href="https://fonts.googleapis.com/css2?family=Quicksand:wght@600;700&family=Source+Sans+3:wght@400&display=swap">
<style>
  :root {
    --ink-navy: #1f3a8f;
    --leaf-blue: #1c9fe0;
    --paper: #ffffff;
  }
  html, body {
    margin: 0;
    padding: 0;
    overflow: hidden;
    background: var(--paper);
  }
  .card {
    position: relative;
    width: 1200px;
    height: 805px;
    background: var(--paper);
    overflow: hidden;
    color: var(--ink-navy);
    font-family: "Quicksand", "Trebuchet MS", sans-serif;
    font-weight: 700;
  }
  .brand {
    position: absolute;
    left: 112px;
    top: 140px;
    display: flex;
    align-items: center;
    gap: 16px;
  }
  .brand-dot {
    width: 44px;
    height: 44px;
    border-radius: 50%;
    background: var(--leaf-blue);
  }
  .brand-name {
    font-size: 48px;
    line-height: 1;
    letter-spacing: 0.5px;
    color: var(--ink-navy);
  }
  .brand-rule {
    position: absolute;
    left: 146px;
    top: 196px;
    width: 331px;
    height: 3px;
    background: var(--leaf-blue);
  }
  .person {
    position: absolute;
    left: 0;
    right: 0;
    top: 328px;
    text-align: center;
  }
  .person-name {
    font-family: "Source Sans 3", "Myriad Pro", sans-serif;
    font-weight: 400;
    font-size: 56px;
    line-height: 1;
    margin: 0;
  }
  .person-role {
    font-size: 24px;
    letter-spacing: 1.5px;
    margin: 8px 0 0;
  }
  .contact {
    position: absolute;
    top: 555px;
    margin: 0;
    font-size: 26px;
    line-height: 34.6px;
    letter-spacing: 1px;
    font-style: normal;
  }
  .contact-details { left: 101px; text-align: left; }
  .contact-address { right: 102px; text-align: right; }
  .contact span { display: block; white-space: pre; }
</style>
</head>
<body>
  <main class="card">
    <div class="brand">
      <span class="brand-dot" aria-hidden="true"></span>
      <span class="brand-name">Fernlo LLP</span>
    </div>
    <div class="brand-rule" aria-hidden="true"></div>

    <section class="person">
      <h1 class="person-name">Tom Harlow</h1>
      <p class="person-role">MANAGING PARTNER</p>
    </section>

    <address class="contact contact-details">
      <span>Email:  tom.harlow@fernlo.co.uk</span>
      <span>Web:  www.fernlo.co.uk</span>
      <span>Tel  +44  (0)1632  960418</span>
      <span>Fax:  (0)1632  960419</span>
      <span>Mobile:  +44  (0)7700  900562</span>
    </address>

    <address class="contact contact-address">
      <span>Enterprise  House</span>
      <span>41  Aldmere  Business  Park</span>
      <span>Harrow  Lane</span>
      <span>Northfield</span>
      <span>NF3  2QT</span>
    </address>
  </main>
</body>
</html>
```